web site to find a reliable, local tradesman, handyman or builder for any job

Design a web site as marketplace for handyman and client.
Handyman can
* set their profile (name, address, contacts)
* search / view / apply for job offers (by setting a new offer)
Client can
* search / view job offers
* generate new job offers (title, description, max price, date, duration, location).
* select and rate a job
Main functions would be SEARCH / VIEW to see in one glance WHAT needs to be done WHERE. The contractors then exchange contacts.
Handyman

```html
<!DOCTYPE html>
<html lang="en">
<head>
<meta charset="utf-8">
<title>Fixora – Find a Handyman</title>
<link rel="stylesheet" href="https://fonts.googleapis.com/css2?family=Ubuntu:wght@400;500;700&family=Arimo:wght@400;700&display=swap">
<style>
:root{
  --navy:#2d4f98;
  --navy-dark:#1f3a7a;
  --orange:#ff9a00;
  --orange-dark:#f07800;
  --sky:#1a8ae6;
  --sky-light:#3fa8f5;
  --text:#333;
  --muted:#666;
  --line:#d9d9d9;
  --bg-top:#dcebf8;
  --footer:#efefef;
}
*{box-sizing:border-box;margin:0;padding:0}
html,body{width:1200px;height:908px;overflow:hidden}
body{position:relative;font-family:"Arimo",Arial,sans-serif;color:var(--text);
  background:linear-gradient(#e3effa 0,#f3f8fd 300px,#fafcfe 489px,#fff 489px,#fff 857px,var(--footer) 857px)}
.abs{position:absolute}
.brand{left:174px;top:22px;font:500 34px "Ubuntu",sans-serif;color:var(--navy);display:flex;align-items:center;gap:8px}
.brand i{width:22px;height:22px;border-radius:50%;background:var(--navy);display:block}
.btn-top{top:25px;height:25px;width:131px;border-radius:3px;color:#fff;font:500 12px "Ubuntu",sans-serif;display:flex;align-items:center;justify-content:center}
.btn-hire{left:754px;background:linear-gradient(var(--sky-light),var(--sky))}
.btn-post{left:893px;background:linear-gradient(#ffb12d,var(--orange-dark))}
.nav{left:174px;top:81px;width:850px;height:41px;background:linear-gradient(#4068b4,var(--navy-dark));border-radius:2px;display:flex}
.nav a{color:#fff;text-decoration:none;font:400 17px "Ubuntu",sans-serif;padding:0 24px;display:flex;align-items:center;border-right:1px solid #4a6db0}
.nav .account{position:absolute;right:7px;top:6px;height:29px;padding:0 9px;border:1px solid #7a95cc;border-radius:2px;background:#355aa6}
.search-panel{left:174px;top:165px;width:225px;height:279px;border:2px solid var(--orange);border-radius:4px;background:#fff}
.search-panel h2{height:41px;background:linear-gradient(#ffa51c,var(--orange-dark));color:#fff;font:700 15px "Ubuntu",sans-serif;padding:13px 11px}
.mascot-badge{left:327px;top:145px;width:65px;height:62px;border-radius:50%;background:radial-gradient(#fff,#c8dcef)}
.field-label{font-size:13px;color:#444}
.box{border:1px solid #ccc;background:linear-gradient(#fff,#f1f1f1);height:28px;font-size:11px;color:#999;padding:7px 10px;border-radius:2px}
.caret{position:absolute;right:0;top:0;width:29px;height:100%;border-left:1px solid #ccc;display:flex;align-items:center;justify-content:center}
.caret:after{content:"";border:4px solid transparent;border-top:5px solid #444;margin-top:4px}
.btn-search{left:184px;top:400px;width:207px;height:34px;border-radius:3px;background:linear-gradient(#ffa51c,var(--orange-dark));color:#fff;font:700 15px "Ubuntu",sans-serif;display:flex;align-items:center;justify-content:center;gap:6px}
.headline{left:418px;top:160px;font:500 29px "Ubuntu",sans-serif;color:var(--orange);white-space:nowrap}
.headline b{color:var(--navy);font-weight:700}
.form-panel{left:418px;top:204px;width:606px;height:276px;background:#fff;box-shadow:0 0 6px rgba(0,0,0,.12)}
.step{left:435px;height:32px;width:170px;color:#fff;font:500 15px "Ubuntu",sans-serif;padding:7px 11px;background:linear-gradient(#ffab20,var(--orange-dark))}
.step.active{width:180px;background:linear-gradient(#4068b4,var(--navy-dark));clip-path:polygon(0 0,172px 0,180px 50%,172px 100%,0 100%)}
.figure{left:560px;top:318px;width:100px;height:158px;border-radius:40px 40px 10px 10px;background:linear-gradient(#6a9be0,#2d4f98)}
.btn-next{left:637px;top:400px;width:365px;height:33px;border-radius:3px;background:linear-gradient(var(--sky-light),#0f74cc);color:#fff;font:500 16px "Ubuntu",sans-serif;display:flex;align-items:center;justify-content:center;letter-spacing:.5px}
.jobbar-line{left:0;top:488px;width:1200px;height:3px;background:var(--navy)}
.jobbar{left:175px;top:491px;width:850px;height:37px;background:linear-gradient(#3f66b2,var(--navy-dark))}
.jobbar h3{position:absolute;left:55px;top:8px;color:#fff;font:700 19px "Ubuntu",sans-serif}
.jobtype{left:418px;top:496px;width:464px;height:26px;background:#fff;border:1px solid #bbb;font:400 15px "Arimo",sans-serif;color:#666;padding:4px 8px}
.adv{position:absolute;right:36px;top:4px;font-size:9px;font-weight:700;color:var(--navy);background:#eee;padding:2px 8px;border-radius:2px}
.btn-go{left:891px;top:495px;width:127px;height:27px;border:1px solid #7a95cc;border-radius:3px;background:#2a4a90;color:#fff;font:700 14px "Ubuntu",sans-serif;display:flex;align-items:center;justify-content:center;letter-spacing:.5px}
.map{left:179px;top:565px;width:214px;height:261px;border-radius:6px;background:linear-gradient(135deg,#e9e5dd,#dcd6c9)}
.map-label{left:216px;top:626px;padding:6px 13px;background:#fff;border-radius:6px;font:400 22px "Ubuntu",sans-serif;color:#333;box-shadow:0 1px 3px rgba(0,0,0,.2)}
.tab{top:561px;height:34px;background:#fff;font:400 15px "Ubuntu",sans-serif;color:#222;display:flex;align-items:center;justify-content:center;border-radius:6px 6px 0 0;box-shadow:0 -1px 2px rgba(0,0,0,.08)}
.tab.active{background:linear-gradient(#4068b4,var(--navy-dark));color:#fff;clip-path:polygon(0 0,164px 0,174px 100%,0 100%);border-radius:0}
.jobs{left:416px;top:595px;width:610px;height:231px;background:#fff;box-shadow:0 1px 4px rgba(0,0,0,.08)}
.col{top:615px;width:128px;list-style:none}
.col li{height:30px;border-bottom:1px dashed #ddd;font-size:9px;color:#444;padding:10px 0 0 20px;position:relative}
.col li:before{content:"›";position:absolute;left:8px;top:8px;color:#777}
.col li.hl{background:#e8eef9;color:var(--navy)}
.divider{top:625px;height:190px;border-left:1px dashed #ddd}
.footer{left:172px;top:877px;display:flex;font-size:9.5px;color:#666}
.footer a{color:#666;text-decoration:none;padding:0 25px;border-right:1px solid #ccc}
.footer a:first-child{padding-left:0}
.footer a:last-child{border:0}
.copy{left:810px;top:878px;font-size:9.5px;color:#666}
</style>
</head>
<body>
<div class="abs brand"><i></i>Fixora</div>
<a class="abs btn-top btn-hire">Hire a Handyman</a>
<a class="abs btn-top btn-post">Post your job</a>

<nav class="abs nav">
  <a>Find Handyman</a><a>Find Work</a><a>How its Work?</a>
  <a class="account">Create account</a>
</nav>

<section class="abs search-panel">
  <h2>Search Handyman</h2>
</section>
<div class="abs mascot-badge" role="img" aria-label="Handyman mascot portrait"></div>
<div class="abs field-label" style="left:183px;top:221px">Select Supplier</div>
<div class="abs box" style="left:183px;top:241px;width:207px">All<span class="caret"></span></div>
<div class="abs field-label" style="left:183px;top:280px">Select Location</div>
<div class="abs box" style="left:183px;top:300px;width:207px">London<span class="caret"></span></div>
<div class="abs field-label" style="left:184px;top:339px">Enter Post Code</div>
<div class="abs box" style="left:183px;top:360px;width:207px;background:#fff">00000</div>
<a class="abs btn-search">
  <svg width="13" height="13" viewBox="0 0 13 13"><circle cx="5.5" cy="5.5" r="4" fill="none" stroke="#fff" stroke-width="2"/><line x1="8.5" y1="8.5" x2="12" y2="12" stroke="#fff" stroke-width="2"/></svg>SEARCH</a>

<h1 class="abs headline"><b>Just 3 simple steps</b> and your job will be posted</h1>
<section class="abs form-panel"></section>
<div class="abs step active" style="top:226px">Job Description</div>
<div class="abs step" style="top:267px">Location &amp; Date</div>
<div class="abs step" style="top:308px">Choose Your Price</div>
<div class="abs figure" role="img" aria-label="Handyman in blue overalls with a red toolbox pointing at the form"></div>

<div class="abs field-label" style="left:637px;top:227px">Type your title</div>
<div class="abs box" style="left:636px;top:250px;width:173px;background:#fff"></div>
<div class="abs field-label" style="left:830px;top:227px">Select your work category</div>
<div class="abs box" style="left:830px;top:250px;width:172px"><span class="caret"></span></div>
<div class="abs field-label" style="left:637px;top:292px">Description</div>
<div class="abs box" style="left:636px;top:311px;width:366px;height:71px;background:#fff"></div>
<a class="abs btn-next">NEXT STEP</a>

<div class="abs jobbar-line"></div>
<section class="abs jobbar">
  <svg class="abs" style="left:18px;top:6px" width="26" height="26" viewBox="0 0 26 26"><circle cx="11" cy="11" r="8" fill="none" stroke="#5aa8ff" stroke-width="3"/><line x1="17" y1="17" x2="24" y2="24" stroke="#5aa8ff" stroke-width="4" stroke-linecap="round"/></svg>
  <h3>Looking For Job?</h3>
</section>
<div class="abs jobtype">Select your job type<span class="adv">Advanced Search</span><span class="caret"></span></div>
<a class="abs btn-go">GO &amp; FIND</a>

<div class="abs map" role="img" aria-label="Street map of the job area"></div>
<div class="abs map-label">UNITED STATE</div>

<div class="abs tab active" style="left:422px;width:174px">Jobs in my category</div>
<div class="abs tab" style="left:583px;width:117px">Top 10 Jobs</div>
<div class="abs tab" style="left:700px;width:134px">Next 10 Jobs</div>
<div class="abs tab" style="left:834px;width:146px">Jobs in my Area</div>
<section class="abs jobs"></section>
<ul class="abs col" style="left:438px">
  <li>Lorem ipsum</li><li>dolor sit amet</li><li>consectetuer adipiscing</li><li>sed diam nonummy</li><li>nibh euismod</li><li>tincidunt ut laoreet</li><li>dolore magna</li>
</ul>
<div class="abs divider" style="left:592px"></div>
<ul class="abs col" style="left:618px">
  <li>Lorem ipsum</li><li>dolor sit amet</li><li class="hl">consectetuer adipiscing</li><li>sed diam nonummy</li><li>nibh euismod</li><li>tincidunt ut laoreet</li><li>dolore magna</li>
</ul>
<div class="abs divider" style="left:773px"></div>
<ul class="abs col" style="left:798px">
  <li>Lorem ipsum</li><li>dolor sit amet</li><li>consectetuer adipiscing</li><li>sed diam nonummy</li>
</ul>

<footer>
  <nav class="abs footer"><a>Home</a><a>Get Quotes</a><a>Testimonials</a><a>About Us</a><a>Contact Us</a><a>Sitemap</a><a>FAQ'S</a></nav>
  <div class="abs copy">© 2011 Company Name</div>
</footer>
</body>
</html>
```